Business Card and Stationary Designs for commercial construction company
Halvern Builders, Inc.
Creative Brief
Use standard fonts
Dennis Whitlock
Director of Operations
6387 Larkmeadow Lane Elk Grove, CA 95731
dennis.whitlock@halvernbldg.com
License #3084519
We like the colors of our logo, so please incorporate them into the card. The font for the other information on the business card does not have to match the logo font, but it should coordinate with it. We need the stationary design to be used to print actual stationary, but we would also like a word document that we can use for creating letters on electronic stationary.

```html
<!DOCTYPE html>
<html lang="en">
<head>
<meta charset="utf-8">
<title>Halvern Builders, Inc. – Business Card</title>
<link rel="stylesheet" href="https://fonts.googleapis.com/css2?family=Montserrat:wght@400;500;700;800&display=swap">
<style>
  :root{
    --page-bg:#e9e7e4;
    --card-white:#ffffff;
    --panel-grey:#8e8e8e;
    --panel-grey-dark:#7a7a7a;
    --brand-red:#e02a32;
    --text-grey:#6d6d6d;
    --text-light:#ffffff;
    --hairline:#c9c9c9;
  }
  *{margin:0;padding:0;box-sizing:border-box;}
  html,body{width:1200px;height:901px;overflow:hidden;}
  body{
    background:var(--page-bg);
    font-family:"Montserrat",Arial,sans-serif;
    position:relative;
  }
  .business-card{
    position:absolute;
    left:150px;top:193px;
    width:900px;height:514px;
    background:var(--card-white);
    border-radius:34px;
    overflow:hidden;
    box-shadow:0 10px 30px rgba(0,0,0,.12);
  }
  .card-art{position:absolute;inset:0;width:100%;height:100%;}
  .brand-lockup{
    position:absolute;left:70px;top:170px;
    display:flex;align-items:center;gap:14px;
  }
  .brand-square{
    width:38px;height:38px;background:var(--panel-grey-dark);
  }
  .brand-name{
    font-weight:800;font-size:42px;letter-spacing:1px;
    color:var(--brand-red);
  }
  .person{
    position:absolute;left:70px;top:326px;
  }
  .person-name{
    font-weight:500;font-size:30px;letter-spacing:1.5px;
    color:var(--brand-red);text-transform:uppercase;
  }
  .person-title{
    margin-top:6px;font-size:20px;color:var(--text-grey);
  }
  .contact-list{
    position:absolute;left:588px;top:70px;width:286px;
    list-style:none;color:var(--text-light);
  }
  .contact-list li{
    display:flex;justify-content:space-between;align-items:center;
    gap:10px;font-size:13.5px;line-height:1.2;
  }
  .contact-list .address{display:block;font-size:16px;margin-bottom:26px;line-height:1.35;}
  .contact-list .line{margin-bottom:12px;}
  .contact-list .web{margin-top:4px;}
  .icon{width:14px;height:14px;flex:none;fill:var(--text-light);}
</style>
</head>
<body>
  <section class="business-card" aria-label="Halvern Builders business card">
    <svg class="card-art" viewBox="0 0 900 514" aria-hidden="true">
      <path d="M610,0 C470,140 540,330 350,514 L900,514 L900,0 Z" fill="var(--panel-grey)"/>
      <path d="M585,0 C445,140 515,330 325,514" fill="none" stroke="var(--brand-red)" stroke-width="12"/>
      <path d="M560,0 C420,140 490,330 300,514" fill="none" stroke="var(--brand-red)" stroke-width="2.5"/>
      <path d="M598,0 C458,140 528,330 338,514" fill="none" stroke="var(--hairline)" stroke-width="2"/>
      <path d="M640,26 L900,26" stroke="var(--brand-red)" stroke-width="3"/>
    </svg>

    <div class="brand-lockup">
      <span class="brand-square"></span>
      <span class="brand-name">HALVERN</span>
    </div>

    <div class="person">
      <p class="person-name">Dennis Whitlock</p>
      <p class="person-title">Director of Operations</p>
    </div>

    <ul class="contact-list">
      <li class="address">6387 Larkmeadow Lane<br>Elk Grove, CA 95731</li>
      <li class="line"><span>916 555 0142</span>
        <svg class="icon" viewBox="0 0 16 16"><path d="M3 1l3 3-2 2c1 2 3 4 5 5l2-2 3 3-2 3C6 14 2 10 1 3z"/></svg></li>
      <li class="line"><span>916 555 0178</span>
        <svg class="icon" viewBox="0 0 16 16"><rect x="4" y="1" width="8" height="14" rx="1.5"/></svg></li>
      <li class="line"><span>License #3084519</span>
        <svg class="icon" viewBox="0 0 16 16"><rect x="2" y="3" width="12" height="10" rx="1"/></svg></li>
      <li class="line"><span>dennis.whitlock@halvernbldg.com</span>
        <svg class="icon" viewBox="0 0 16 16"><path d="M1 3h14v10H1z M1 3l7 6 7-6" fill="none" stroke="#fff" stroke-width="1.5"/></svg></li>
      <li class="web"><span>www.halvernbldg.com</span>
        <svg class="icon" viewBox="0 0 16 16"><circle cx="8" cy="8" r="7"/></svg></li>
    </ul>
  </section>
</body>
</html>
```